Dorsey K. Wendell Business Card

We need a business card for our company Dorsey K. Wendell Heating & Plumbing to be distributed to potential customers. It should follow the color scheme of our logo and have a modern upscale and masculine look.

The logo is attached and the info below should also be included:

5187 W. Cedar Brook Rd.
Fernhollow, PA 17980

Russell T. Wendell
(717) 592-0817
russelltwendell@fernmail.net
dorseykwendell.net
PA #093148

Industry/Entity Type

Business

Contact Information for Business Card

5187 W. Cedar Brook Rd.
Fernhollow, PA 17980

Russell T. Wendell
(717) 592-0817
russelltwendell@fernmail.net
dorseykwendell.net
PA #093148

Colors

Designer to choose colors to be used in the design.

Requirements
Must have
• Information above included

```html
<!DOCTYPE html>
<html lang="en">
<head>
<meta charset="utf-8">
<title>Dorsey K. Wendell Business Card</title>
<link href="https://fonts.googleapis.com/css2?family=Source+Sans+3:wght@400;600;700&display=swap" rel="stylesheet">
<style>
  :root {
    --card-black: #070707;
    --brand-blue: #1f5fb4;
    --brand-green: #a9c93b;
    --text-white: #f4f4f4;
    --backdrop: #e9e7e3;
  }
  * { margin: 0; padding: 0; box-sizing: border-box; }
  html, body { width: 1200px; height: 1200px; overflow: hidden; }
  body {
    background: var(--backdrop);
    font-family: "Source Sans 3", "Helvetica Neue", Arial, sans-serif;
    display: flex;
    flex-direction: column;
    align-items: center;
    justify-content: center;
    gap: 44px;
  }
  .card {
    position: relative;
    width: 940px;
    height: 537px;
    background: var(--card-black);
    overflow: hidden;
    box-shadow: 0 6px 18px rgba(0,0,0,0.18);
  }
  .brand {
    display: flex;
    align-items: center;
    gap: 22px;
    color: var(--brand-blue);
    font-weight: 700;
    text-transform: uppercase;
    letter-spacing: 0.02em;
  }
  .brand-square {
    background: var(--brand-blue);
    flex: none;
  }
  .card-front .brand {
    position: absolute;
    left: 50%; top: 50%;
    transform: translate(-50%, -50%);
    font-size: 46px;
    line-height: 1.05;
    white-space: nowrap;
  }
  .card-front .brand-square { width: 84px; height: 84px; }

  .card-back .brand {
    position: absolute;
    left: 50%; top: 58px;
    transform: translateX(-50%);
    font-size: 36px;
    line-height: 1.05;
    white-space: nowrap;
  }
  .card-back .brand-square { width: 66px; height: 66px; }

  .holder-name {
    position: absolute;
    left: 0; right: 0; top: 200px;
    text-align: center;
    color: var(--brand-green);
    font-size: 46px;
    font-weight: 600;
    text-transform: uppercase;
    letter-spacing: 0.01em;
  }
  .address {
    position: absolute;
    left: 0; right: 0; top: 272px;
    text-align: center;
    color: var(--text-white);
    font-size: 27px;
  }
  .contact-grid {
    position: absolute;
    left: 0; right: 0; top: 330px;
    display: flex;
    justify-content: center;
    align-items: stretch;
    gap: 26px;
    color: var(--text-white);
    font-size: 27px;
    line-height: 1.5;
  }
  .contact-col-left { text-align: right; }
  .contact-col-right { text-align: left; }
  .contact-divider { width: 2px; background: var(--brand-green); }
  .label { color: var(--brand-green); }
  .accent-line {
    position: absolute;
    left: 0; right: 0; bottom: 44px;
    height: 2px;
    background: var(--brand-green);
  }
  .accent-band {
    position: absolute;
    left: 0; right: 0; bottom: 0;
    height: 30px;
    background: var(--brand-blue);
  }
</style>
</head>
<body>
  <section class="card card-front" aria-label="Card front">
    <div class="brand">
      <span class="brand-square"></span>
      <span class="brand-name">Dorsey K. Wendell<br>Heating &amp; Plumbing</span>
    </div>
  </section>

  <section class="card card-back" aria-label="Card back">
    <div class="brand">
      <span class="brand-square"></span>
      <span class="brand-name">Dorsey K. Wendell<br>Heating &amp; Plumbing</span>
    </div>
    <h1 class="holder-name">Russell T. Wendell</h1>
    <p class="address">5187 W. Cedar Brook Rd. Fernhollow, PA 17980</p>
    <div class="contact-grid">
      <div class="contact-col-left">
        <div><span class="label">PA #</span> 093148</div>
        <div>www.dorseykwendell.net</div>
      </div>
      <div class="contact-divider"></div>
      <div class="contact-col-right">
        <div><span class="label">Tel #</span> (717) 592-0817</div>
        <div>russelltwendell@fernmail.net</div>
      </div>
    </div>
    <div class="accent-line"></div>
    <div class="accent-band"></div>
  </section>
</body>
</html>
```